Remote Planning & Scheduling Power Point Presentation

This PP presentation is to help explain what RPS is and its benefits. Need help with a better illustration on slide 3 that explains the process, overall aesthetics, need better images, and cleaner workflow on slide 18. Keep the DEW Logo in the bottom right of each slide. I have included a one-pager and infographic to help. I am still working of verbiage.

Thanks
SL

```html
<!DOCTYPE html>
<html lang="en">
<head>
<meta charset="utf-8">
<title>RPS Flow Process</title>
<link rel="stylesheet" href="https://fonts.googleapis.com/css2?family=Didact+Gothic&family=Open+Sans:wght@600;700&display=swap">
<style>
  :root {
    --page: #ffffff;
    --frame: #e4e4e4;
    --slide-edge: #c9c9c9;
    --banner-blue: #0a2f88;
    --banner-slate: #47525e;
    --banner-slate-light: #5a6571;
    --band-light: #f1f1f1;
    --band-dark: #cdcdcd;
    --label: #3a3a3a;
    --red: #c8233b;
    --teal: #1c9a88;
    --blue: #2c86c8;
    --purple: #7a1a58;
    --mark: #d2d2d2;
    --white: #ffffff;
  }
  * { margin: 0; padding: 0; box-sizing: border-box; }
  html, body { width: 1200px; height: 681px; overflow: hidden; background: var(--page); }
  .slide-canvas { display: block; width: 1200px; height: 681px; }
  .slide-title { font-family: "Didact Gothic", sans-serif; fill: var(--white); font-size: 28px; }
  .step-label { font-family: "Open Sans", sans-serif; font-weight: 700; font-size: 5.6px; fill: var(--label); }
  .hex-caption { font-family: "Open Sans", sans-serif; font-weight: 700; font-size: 6.8px; fill: var(--white); text-anchor: middle; }
  .band { fill: url(#bandShade); }
  .hex-shadow { fill: #000000; opacity: 0.22; }
  .icon { fill: none; stroke: var(--white); stroke-width: 1.5; stroke-linecap: round; stroke-linejoin: round; }
  .icon-solid { fill: var(--white); }
  .brand-name { font-family: "Didact Gothic", sans-serif; font-size: 30px; fill: var(--mark); letter-spacing: 2px; }
</style>
</head>
<body>
<svg class="slide-canvas" viewBox="0 0 960 540" preserveAspectRatio="none" xmlns="http://www.w3.org/2000/svg">
  <defs>
    <linearGradient id="bandShade" x1="0" y1="0" x2="0" y2="1">
      <stop offset="0" stop-color="var(--band-light)"/>
      <stop offset="1" stop-color="var(--band-dark)"/>
    </linearGradient>
    <linearGradient id="bandShadeV" x1="0" y1="0" x2="1" y2="0">
      <stop offset="0" stop-color="var(--band-light)"/>
      <stop offset="1" stop-color="var(--band-dark)"/>
    </linearGradient>
    <radialGradient id="hexGloss" cx="0.4" cy="0.3" r="0.8">
      <stop offset="0" stop-color="#ffffff" stop-opacity="0.28"/>
      <stop offset="1" stop-color="#000000" stop-opacity="0.15"/>
    </radialGradient>
    <polygon id="hexFlat" points="1,0 0.5,0.866 -0.5,0.866 -1,0 -0.5,-0.866 0.5,-0.866"/>
    <polygon id="hexPoint" points="0,-1 0.866,-0.5 0.866,0.5 0,1 -0.866,0.5 -0.866,-0.5"/>
    <g id="calendarIcon">
      <rect class="icon" x="-7" y="-6" width="14" height="13"/>
      <path class="icon" d="M-7,-2.5 h14 M-3.5,-9 v4 M3.5,-9 v4"/>
      <path d="M-4.5,1 h2 M-1,1 h2 M2.5,1 h2 M-4.5,4.5 h2 M-1,4.5 h2 M2.5,4.5 h2" stroke="var(--white)" stroke-width="1.4"/>
    </g>
    <g id="pairIcon" class="icon-solid">
      <circle cx="-4.5" cy="-3.5" r="3.2"/><circle cx="4.5" cy="-3.5" r="3.2"/>
      <path d="M-10,7 q0,-7 5.5,-7 q5.5,0 5.5,7 z M0,7 q0,-7 5.5,-7 q5.5,0 5.5,7 z"/>
    </g>
    <g id="groupIcon" class="icon-solid">
      <circle cx="-6" cy="-4" r="3.6"/><circle cx="6" cy="-4" r="3.6"/><circle cx="0" cy="-1.5" r="4.2"/>
      <path d="M-13,9 q0,-8 7,-8 h12 q7,0 7,8 z"/>
    </g>
  </defs>

  <!-- frame and slide -->
  <rect x="48" y="33" width="824" height="475" fill="var(--frame)"/>
  <rect x="55" y="41" width="810" height="458" fill="var(--page)" stroke="var(--slide-edge)" stroke-width="0.8"/>

  <!-- title banner -->
  <g class="title-banner">
    <rect x="86" y="72" width="750" height="117" fill="var(--banner-blue)"/>
    <polygon points="650,72 836,72 836,189 572,189" fill="var(--banner-slate)"/>
    <polygon points="742,76 822,189 662,189" fill="var(--banner-slate-light)"/>
    <text class="slide-title" x="140" y="140">RPS Flow Process</text>
  </g>

  <!-- connector bands -->
  <g class="flow-bands">
    <rect class="band" x="140" y="218" width="606" height="26"/>
    <rect x="728" y="232" width="32" height="106" fill="url(#bandShadeV)"/>
    <rect class="band" x="140" y="307" width="620" height="31"/>
    <rect x="122" y="320" width="32" height="106" fill="url(#bandShadeV)"/>
    <rect class="band" x="122" y="395" width="638" height="31"/>
    <g fill="#ffffff" opacity="0.6">
      <polygon points="292,218 299,231 292,244 296,244 303,231 296,218"/>
      <polygon points="428,218 435,231 428,244 432,244 439,231 432,218"/>
      <polygon points="562,218 569,231 562,244 566,244 573,231 566,218"/>
      <polygon points="700,218 707,231 700,244 704,244 711,231 704,218"/>
      <polygon points="668,307 660,322 668,337 664,337 656,322 664,307"/>
      <polygon points="448,307 440,322 448,337 444,337 436,322 444,307"/>
      <polygon points="310,307 302,322 310,337 306,337 298,322 306,307"/>
      <polygon points="182,307 174,322 182,337 178,337 170,322 178,307"/>
      <polygon points="300,395 308,410 300,425 304,425 312,410 304,395"/>
      <polygon points="450,395 458,410 450,425 454,425 462,410 454,395"/>
      <polygon points="572,395 580,410 572,425 576,425 584,410 576,395"/>
      <polygon points="708,395 716,410 708,425 712,425 720,410 712,395"/>
    </g>
  </g>

  <!-- step labels -->
  <g class="step-labels">
    <text class="step-label" x="246" y="234">Collect Worklist</text>
    <text class="step-label" x="376" y="234">Scope Review</text>
    <text class="step-label" x="509" y="234">Planning Premise</text>
    <text class="step-label" x="644" y="234">Data Collection</text>
    <text class="step-label" x="694" y="323">Field Photos</text>
    <text class="step-label" x="457" y="323">Detail Planning</text>
    <text class="step-label" x="324" y="325">Develop Package</text>
    <text class="step-label" x="188" y="323">Package Review</text>
    <text class="step-label" transform="translate(136,354) rotate(90)">Package Acceptance</text>
    <text class="step-label" x="260" y="411">Level 1</text>
    <text class="step-label" x="388" y="411">Schedule Review</text>
    <text class="step-label" x="528" y="408">Level 2</text>
    <text class="step-label" x="652" y="409">Schedule Review</text>
  </g>

  <!-- hexagon steps -->
  <g class="flow-steps">
    <!-- On Site -->
    <g transform="translate(136,231)">
      <use href="#hexFlat" class="hex-shadow" transform="translate(1.5,2.5) scale(39)"/>
      <use href="#hexFlat" transform="scale(39)" fill="var(--white)"/>
      <use href="#hexFlat" transform="scale(34)" fill="var(--red)"/>
      <use href="#hexFlat" transform="scale(34)" fill="url(#hexGloss)"/>
      <use href="#groupIcon" transform="translate(4,-9)"/>
      <path class="icon" d="M-20,-10 v10 M-23,-3 l3,3 l3,-3 M-24,4 h8"/>
      <text class="hex-caption" x="4" y="15">On Site</text>
    </g>
    <!-- Collect Worklist -->
    <g transform="translate(211,231)">
      <use href="#hexFlat" class="hex-shadow" transform="translate(1.5,2.5) scale(26)"/>
      <use href="#hexFlat" transform="scale(26)" fill="var(--white)"/>
      <use href="#hexFlat" transform="scale(22)" fill="var(--teal)"/>
      <use href="#hexFlat" transform="scale(22)" fill="url(#hexGloss)"/>
      <path class="icon" d="M-5,-6 h12 M-5,0 h12 M-5,6 h12"/>
      <g class="icon-solid"><circle cx="-9" cy="-6" r="1.3"/><circle cx="-9" cy="0" r="1.3"/><circle cx="-9" cy="6" r="1.3"/></g>
    </g>
    <!-- Scope Review -->
    <g transform="translate(344,231)">
      <use href="#hexFlat" class="hex-shadow" transform="translate(1.5,2.5) scale(26)"/>
      <use href="#hexFlat" transform="scale(26)" fill="var(--white)"/>
      <use href="#hexFlat" transform="scale(22)" fill="var(--blue)"/>
      <use href="#hexFlat" transform="scale(22)" fill="url(#hexGloss)"/>
      <g class="icon-solid"><circle cx="-5.5" cy="3" r="5.5"/><circle cx="5.5" cy="3" r="5.5"/><rect x="-8.5" y="-8" width="5.5" height="9"/><rect x="3" y="-8" width="5.5" height="9"/><rect x="-3" y="-4" width="6" height="4"/></g>
    </g>
    <!-- Planning Premise -->
    <g transform="translate(478,231)">
      <use href="#hexFlat" class="hex-shadow" transform="translate(1.5,2.5) scale(26)"/>
      <use href="#hexFlat" transform="scale(26)" fill="var(--white)"/>
      <use href="#hexFlat" transform="scale(22)" fill="var(--purple)"/>
      <use href="#hexFlat" transform="scale(22)" fill="url(#hexGloss)"/>
      <rect x="-6.5" y="-9" width="13" height="18" class="icon-solid"/>
      <path d="M-3.5,-4.5 h7 M-3.5,-0.5 h7 M-3.5,3.5 h7" stroke="var(--purple)" stroke-width="1.3"/>
    </g>
    <!-- Data Collection -->
    <g transform="translate(612,231)">
      <use href="#hexFlat" class="hex-shadow" transform="translate(1.5,2.5) scale(26)"/>
      <use href="#hexFlat" transform="scale(26)" fill="var(--white)"/>
      <use href="#hexFlat" transform="scale(22)" fill="var(--red)"/>
      <use href="#hexFlat" transform="scale(22)" fill="url(#hexGloss)"/>
      <rect class="icon" x="-6.5" y="-8.5" width="13" height="17"/>
      <path class="icon" d="M-3.5,-4 h7 M-3.5,0 h7 M-3.5,4 h5"/>
    </g>
    <!-- Field Photos -->
    <g transform="translate(744,233)">
      <use href="#hexPoint" class="hex-shadow" transform="translate(1.5,2.5) scale(29)"/>
      <use href="#hexPoint" transform="scale(29)" fill="var(--white)"/>
      <use href="#hexPoint" transform="scale(25)" fill="var(--purple)"/>
      <use href="#hexPoint" transform="scale(25)" fill="url(#hexGloss)"/>
      <rect class="icon" x="-9.5" y="-5" width="19" height="13" rx="2"/>
      <circle class="icon" cx="0" cy="1.5" r="3.8"/>
      <path class="icon" d="M-4,-5 l2,-3 h4 l2,3"/>
    </g>
    <!-- Remote, mid row -->
    <g transform="translate(604,320)">
      <use href="#hexFlat" class="hex-shadow" transform="translate(1.5,2.5) scale(40)"/>
      <use href="#hexFlat" transform="scale(40)" fill="var(--white)"/>
      <use href="#hexFlat" transform="scale(35)" fill="var(--blue)"/>
      <use href="#hexFlat" transform="scale(35)" fill="url(#hexGloss)"/>
      <use href="#groupIcon" transform="translate(0,-12)"/>
      <text class="hex-caption" x="0" y="11">Remote</text>
      <circle cx="0" cy="20" r="1.4" class="icon-solid"/>
      <path class="icon" d="M-4,17 a5,5 0 0 0 0,6 M4,17 a5,5 0 0 1 0,6" stroke-width="1.1"/>
    </g>
    <!-- Detail Planning -->
    <g transform="translate(529,320)">
      <use href="#hexFlat" class="hex-shadow" transform="translate(1.5,2.5) scale(26)"/>
      <use href="#hexFlat" transform="scale(26)" fill="var(--white)"/>
      <use href="#hexFlat" transform="scale(22)" fill="var(--teal)"/>
      <use href="#hexFlat" transform="scale(22)" fill="url(#hexGloss)"/>
      <path class="icon" d="M0,0 L-6,-6 M0,0 L6,-6 M0,0 L-6,6 M0,0 L6,6"/>
      <g class="icon"><circle cx="0" cy="0" r="2.8"/><circle cx="-7.5" cy="-7.5" r="2.3"/><circle cx="7.5" cy="-7.5" r="2.3"/><circle cx="-7.5" cy="7.5" r="2.3"/><circle cx="7.5" cy="7.5" r="2.3"/></g>
    </g>
    <!-- Develop Package -->
    <g transform="translate(399,320)">
      <use href="#hexFlat" class="hex-shadow" transform="translate(1.5,2.5) scale(26)"/>
      <use href="#hexFlat" transform="scale(26)" fill="var(--white)"/>
      <use href="#hexFlat" transform="scale(22)" fill="var(--red)"/>
      <use href="#hexFlat" transform="scale(22)" fill="url(#hexGloss)"/>
      <circle class="icon" cx="0" cy="0" r="7.5"/>
      <g class="icon-solid"><circle cx="0" cy="-9.5" r="2"/><circle cx="8.5" cy="-3.5" r="2"/><circle cx="6.5" cy="6.5" r="2"/><circle cx="-6.5" cy="6.5" r="2"/><circle cx="-8.5" cy="-3.5" r="2"/></g>
    </g>
    <!-- Package Review -->
    <g transform="translate(267,320)">
      <use href="#hexFlat" class="hex-shadow" transform="translate(1.5,2.5) scale(26)"/>
      <use href="#hexFlat" transform="scale(26)" fill="var(--white)"/>
      <use href="#hexFlat" transform="scale(22)" fill="var(--blue)"/>
      <use href="#hexFlat" transform="scale(22)" fill="url(#hexGloss)"/>
      <rect class="icon" x="-9" y="-7" width="18" height="14"/>
      <path class="icon" d="M-6,-3.5 h7"/>
      <circle class="icon" cx="3" cy="2" r="2.8"/>
      <path class="icon" d="M5,4 l3.5,3.5"/>
    </g>
    <!-- Package Acceptance -->
    <g transform="translate(138,320)">
      <use href="#hexPoint" class="hex-shadow" transform="translate(1.5,2.5) scale(30)"/>
      <use href="#hexPoint" transform="scale(30)" fill="var(--white)"/>
      <use href="#hexPoint" transform="scale(26)" fill="var(--purple)"/>
      <use href="#hexPoint" transform="scale(26)" fill="url(#hexGloss)"/>
      <path class="icon" d="M-8,2 l5.5,-5.5 l4.5,4.5 l-5.5,5.5 z M2,-8 l5.5,5.5 l-4.5,4.5"/>
    </g>
    <!-- Level 1 -->
    <g transform="translate(216,409)">
      <use href="#hexFlat" class="hex-shadow" transform="translate(1.5,2.5) scale(26)"/>
      <use href="#hexFlat" transform="scale(26)" fill="var(--white)"/>
      <use href="#hexFlat" transform="scale(22)" fill="var(--red)"/>
      <use href="#hexFlat" transform="scale(22)" fill="url(#hexGloss)"/>
      <use href="#calendarIcon"/>
    </g>
    <!-- Schedule Review -->
    <g transform="translate(349,409)">
      <use href="#hexFlat" class="hex-shadow" transform="translate(1.5,2.5) scale(26)"/>
      <use href="#hexFlat" transform="scale(26)" fill="var(--white)"/>
      <use href="#hexFlat" transform="scale(22)" fill="var(--teal)"/>
      <use href="#hexFlat" transform="scale(22)" fill="url(#hexGloss)"/>
      <use href="#pairIcon"/>
    </g>
    <!-- Level 2 -->
    <g transform="translate(484,408)">
      <use href="#hexFlat" class="hex-shadow" transform="translate(1.5,2.5) scale(26)"/>
      <use href="#hexFlat" transform="scale(26)" fill="var(--white)"/>
      <use href="#hexFlat" transform="scale(22)" fill="var(--teal)"/>
      <use href="#hexFlat" transform="scale(22)" fill="url(#hexGloss)"/>
      <use href="#calendarIcon"/>
    </g>
    <!-- Schedule Review, second -->
    <g transform="translate(616,407)">
      <use href="#hexFlat" class="hex-shadow" transform="translate(1.5,2.5) scale(26)"/>
      <use href="#hexFlat" transform="scale(26)" fill="var(--white)"/>
      <use href="#hexFlat" transform="scale(22)" fill="var(--red)"/>
      <use href="#hexFlat" transform="scale(22)" fill="url(#hexGloss)"/>
      <use href="#pairIcon"/>
    </g>
    <!-- Remote, final -->
    <g transform="translate(768,412)">
      <use href="#hexFlat" class="hex-shadow" transform="translate(1.5,2.5) scale(42)"/>
      <use href="#hexFlat" transform="scale(42)" fill="var(--white)"/>
      <use href="#hexFlat" transform="scale(37)" fill="var(--blue)"/>
      <use href="#hexFlat" transform="scale(37)" fill="url(#hexGloss)"/>
      <use href="#calendarIcon" transform="translate(0,-9)"/>
      <text class="hex-caption" x="0" y="12">Remote</text>
    </g>
  </g>

  <!-- brand mark -->
  <text class="brand-name" x="786" y="478">DEW</text>
</svg>
</body>
</html>
```